Equipment Supplier Brochure Needed

We need a professional one-page, front-and-back brochure for Tovrik, an equipment and parts supplier serving peanut shelling and processing facilities across the Southeast. This brochure will be used as a leave-behind with plant managers and procurement teams, so it must look clean, modern, and visually strong.

Front of brochure:

Tovrik logo and strong branding

Brief headline/summary of what Tovrik does

Product category overview listed on the front (high-level, clean layout)

Flat Screens (slot, round, herringbone, square, Style 1 & Style 2)

Sheller Grates

Ripple Screens

Sheller Bars

Eccentric Bearing Housings

Eccentric Shafts

Rebuilt Machines

Ducts

Sprockets

Rubber Gum Balls

Fiberglass

Wilmot Penn Reels

Elevator Buckets

Space for several product photos (we’ve uploaded images)

Clean industrial aesthetic

Back of brochure:

More detailed visual layout of products

Strong callout section showing companies we represent (logos included)

Optional short paragraph about Tovrik’s capabilities, history, or differentiators

Contact info section

Overall style:

Clean, modern, print-ready

Industrial yet polished

Balanced visual + text layout

Color palette aligned with Tovrik brand

Final files delivered as print-ready PDF (plus editable source file if available)

We’ve uploaded product imagery, partner logos, and reference materials. Please design multiple layout concepts if possible.

```html
<!DOCTYPE html>
<html lang="en">
<head>
<meta charset="utf-8">
<title>Tovrik Brochure – Front and Back</title>
<link rel="stylesheet" href="https://fonts.googleapis.com/css2?family=Michroma&family=Montserrat:wght@400;500;600;700;800&display=swap">
<style>
:root{
  --blue:#1b4fa8;
  --navy:#123a82;
  --cyan:#37c2ec;
  --ink:#1d1d1f;
  --black:#141414;
  --paper:#f4f5f8;
  --stage:#dcdcdc;
  --muted:#4a4a4a;
  --line:#c9ced8;
}
*{margin:0;padding:0;box-sizing:border-box}
html,body{width:1200px;height:844px;overflow:hidden;background:var(--stage);font-family:"Montserrat",sans-serif;color:var(--ink)}
.page{position:absolute;top:106px;width:490px;height:633px;background:var(--paper);overflow:hidden}
.page--front{left:68px}
.page--back{left:643px}
.abs{position:absolute}
.photo{position:absolute}
.heading{font-family:"Michroma",sans-serif;color:var(--blue);letter-spacing:.5px}

/* front */
.hero-photo{left:150px;top:0;width:340px;height:156px;background:linear-gradient(135deg,#caa57a,#b9844d 45%,#8a5a2c)}
.brand{left:26px;top:20px;font-family:"Montserrat",sans-serif;font-weight:800;font-size:30px;color:var(--blue);letter-spacing:1px}
.hero-band{left:0;top:0;width:490px;height:200px}
.tagline{left:25px;top:74px;color:var(--cyan);font-family:"Michroma",sans-serif;font-size:10px;line-height:11px}
.headline{left:25px;top:100px;color:#fff;font-family:"Michroma",sans-serif;font-size:16.5px;line-height:19px;font-weight:400}
.tile{position:absolute;width:92px;height:91px;border:2px solid var(--cyan);background:linear-gradient(160deg,#8d8f93,#55585e)}
.tile-label{position:absolute;left:4px;bottom:0;right:0;height:14px;background:var(--blue);border-radius:7px 0 0 0;color:#fff;font-size:7.5px;font-weight:500;text-align:center;line-height:14px}
.tile-label--cyan{background:var(--cyan);color:var(--ink)}
.product-title{left:244px;top:180px;font-size:14.5px}
.product-list{position:absolute;list-style:none;width:118px}
.product-list li{position:relative;padding:0 0 5px 12px;margin-bottom:7px;border-bottom:1px solid var(--line);font-size:7.6px;font-weight:500;line-height:9.5px;color:var(--ink)}
.product-list li::before{content:"";position:absolute;left:0;top:1px;width:7px;height:7px;border-radius:50%;background:var(--blue)}
.welding-photo{left:246px;top:405px;width:216px;height:131px;border:2px solid var(--blue);background:linear-gradient(135deg,#3d5070,#7a8aa3 50%,#2a3345)}
.footer-shape{left:0;top:540px;width:490px;height:93px}
.contact{color:#fff;font-size:9.5px;font-weight:500;line-height:11px}
.contact svg{vertical-align:-2px;margin-right:2px}
.web{color:#fff;font-size:12px;letter-spacing:3.2px;font-weight:500}
.web b{color:var(--cyan);font-weight:700}

/* back */
.story-bg{left:0;top:0;width:490px;height:262px;background:linear-gradient(180deg,#2b2b2d,#4b4c4f 60%,#6b6d70)}
.story-title{left:0;width:490px;top:22px;text-align:center;color:var(--cyan);font-size:19px}
.story-lead{left:40px;width:410px;top:55px;text-align:center;color:#fff;font-size:8.6px;font-weight:700;line-height:11.5px}
.story-text{left:40px;width:410px;top:103px;text-align:center;color:#eee;font-size:8.8px;line-height:11.6px}
.shop-photo{top:180px;width:132px;height:130px;border:3px solid #fff;background:linear-gradient(150deg,#a79a86,#6f6a63 55%,#3e3b38)}
.services-title{left:25px;top:317px;font-size:19.5px;color:var(--navy)}
.services-text{left:25px;top:350px;width:428px;font-size:9.5px;line-height:11.6px}
.service{position:absolute;width:140px}
.service-pill{position:relative;height:17px;border-radius:9px;background:var(--cyan);color:#fff;font-size:7.2px;font-weight:600;line-height:7.5px;padding:1px 8px 0 25px;display:flex;align-items:center}
.service-pill--dark{background:var(--blue)}
.service-icon{position:absolute;left:-1px;top:-2px;width:21px;height:21px;border-radius:50%;background:var(--blue);border:2px solid #fff;box-shadow:0 0 0 1px var(--blue)}
.service p{margin-top:6px;font-size:7px;line-height:8.6px;color:var(--muted);padding-right:8px}
.divider-v{position:absolute;width:1px;background:var(--line)}
.partner{position:absolute;display:flex;align-items:center;justify-content:center;width:88px;height:28px;font-size:9px;font-weight:700;color:#333;letter-spacing:.5px}
</style>
</head>
<body>

<!-- FRONT -->
<section class="page page--front">
  <div class="photo hero-photo" role="img" aria-label="Close-up of raw peanuts on a processing line"></div>
  <svg class="abs hero-band" viewBox="0 0 490 200" aria-hidden="true">
    <polygon points="0,0 150,0 150,70 0,70" fill="#ffffff"/>
    <polygon points="150,0 200,0 150,60" fill="#ffffff"/>
    <polygon points="0,69 240,69 314,152 490,152 490,160 308,160 276,188 0,188" fill="#1b4fa8"/>
    <polygon points="276,188 308,160 490,160 490,162 310,162 280,190" fill="#123a82"/>
    <circle cx="211" cy="188" r="1.8" fill="#141414"/>
    <line x1="211" y1="188" x2="276" y2="188" stroke="#141414" stroke-width=".6"/>
  </svg>
  <div class="abs brand">TOVRIK</div>
  <div class="abs tagline">We Manufacture<br>&amp; Supply</div>
  <h1 class="abs headline">REPLACEMENT<br>PARTS FOR<br>PEANUT PROCESSING<br>EQUIPMENT</h1>

  <div class="tile" style="left:26px;top:206px" role="img" aria-label="Flat screens stacked on a rack"><span class="tile-label">Flat Screens</span></div>
  <div class="tile" style="left:131px;top:206px" role="img" aria-label="Sheller grates"><span class="tile-label tile-label--cyan">Sheller Grates</span></div>
  <div class="tile" style="left:26px;top:306px" role="img" aria-label="Eccentric shafts"><span class="tile-label tile-label--cyan">Eccentric Shafts</span></div>
  <div class="tile" style="left:131px;top:306px" role="img" aria-label="Ripple screen surface"><span class="tile-label">Ripple Screens</span></div>
  <div class="tile" style="left:26px;top:409px" role="img" aria-label="Rubber gum balls"><span class="tile-label">Rubber Gum Balls</span></div>
  <div class="tile" style="left:131px;top:409px" role="img" aria-label="Rebuilt machines in the shop"><span class="tile-label tile-label--cyan">Rebuilt Machines</span></div>
  <div class="tile" style="left:26px;top:509px" role="img" aria-label="Elevator buckets"><span class="tile-label tile-label--cyan">Elevator Buckets</span></div>
  <div class="tile" style="left:131px;top:509px" role="img" aria-label="Sprockets"><span class="tile-label">Sprockets</span></div>

  <h2 class="abs heading product-title">OUR PRODUCT</h2>
  <ul class="product-list" style="left:244px;top:206px;width:120px">
    <li>Flat Screens (slot, round, herringbone, square, Style 1 &amp; Style 2)</li>
    <li>Eccentric Shafts</li>
    <li>Sheller Grates</li>
    <li>Ripple Screens</li>
    <li>Sheller Bars</li>
    <li>Rubber Gum Balls</li>
    <li>Wilmot Penn Reels</li>
  </ul>
  <ul class="product-list" style="left:380px;top:206px;width:85px">
    <li>Eccentric Bearing Housings</li>
    <li>Rebuilt Machines</li>
    <li>Ducts</li>
    <li>Sprockets</li>
    <li>Fiberglass</li>
    <li style="border-bottom:none">Elevator Buckets</li>
  </ul>

  <div class="photo welding-photo" role="img" aria-label="Worker welding a steel part"></div>

  <svg class="abs footer-shape" viewBox="0 0 490 93" aria-hidden="true">
    <polygon points="270,12 490,12 490,78 200,78" fill="#141414"/>
    <polygon points="262,9 490,9 490,12 268,12 197,78 190,78" fill="#1b4fa8"/>
    <polygon points="0,78 490,78 490,93 0,93" fill="#1b4fa8"/>
  </svg>
  <div class="abs contact" style="left:279px;top:573px">
    <svg width="9" height="9" viewBox="0 0 10 10"><circle cx="5" cy="5" r="5" fill="#37c2ec"/><circle cx="5" cy="4.2" r="1.6" fill="#141414"/></svg>418 W Mill Street
    &nbsp;<svg width="9" height="9" viewBox="0 0 10 10"><circle cx="5" cy="5" r="5" fill="#37c2ec"/><path d="M3.3 2.8l1 1-.5.7a3 3 0 0 0 1.7 1.7l.7-.5 1 1-.7.8A4.5 4.5 0 0 1 2.6 3.5z" fill="#141414"/></svg>(334) 555-0142<br>
    &nbsp;&nbsp;&nbsp;Ardenville, AL 36390
  </div>
  <div class="abs web" style="left:278px;top:601px">www.<b>tovrik-inc</b>.com</div>
</section>

<!-- BACK -->
<section class="page page--back">
  <div class="photo story-bg" role="img" aria-label="Dark view of the fabrication facility building"></div>
  <h2 class="abs heading story-title">OUR STORY</h2>
  <p class="abs story-lead">We believe in simple small town values like hard work, community and quality. That's why you'll find our team working day in and day out to provide our customers with quality products</p>
  <p class="abs story-text">Our replacement parts are designed and manufactured in our fabrication facility in Ardenville, AL. With our American made parts, you can be assured of quality, availability and on-time delivery. Our parts are fabricated to exact customer specifications. Plus, unlike large corporations and foreign manufactures, we are easy to reach if you need to talk to someone.</p>

  <div class="photo shop-photo" style="left:23px" role="img" aria-label="Machinist operating a milling machine"></div>
  <div class="photo shop-photo" style="left:177px" role="img" aria-label="Worker cutting sheet metal on a press"></div>
  <div class="photo shop-photo" style="left:333px" role="img" aria-label="Worker grinding steel with sparks"></div>

  <h2 class="abs heading services-title">OUR SERVICES</h2>
  <p class="abs services-text">Our replacement parts are designed and manufactured in our fabrication facility in Ardenville, AL. With our American made parts, you can be assured of quality, availability and on-time delivery. Our parts are fabricated to exact customer specifications. Plus, unlike large corporations and foreign manufactures, we are easy to reach if you need to talk to someone.</p>

  <div class="divider-v" style="left:166px;top:414px;height:125px"></div>
  <div class="divider-v" style="left:324px;top:414px;height:125px"></div>

  <div class="service" style="left:26px;top:414px"><div class="service-pill service-pill--dark"><span class="service-icon"></span>Replacement Parts Manufacturing</div><p>We manufacture replacement parts to customers' specifications.</p></div>
  <div class="service" style="left:186px;top:414px"><div class="service-pill"><span class="service-icon"></span>Replacement Parts Distribution</div><p>We are distributors for Wilmot Penn International, Keystone Elevator, and Brannock Screen Company</p></div>
  <div class="service" style="left:340px;top:414px"><div class="service-pill service-pill--dark"><span class="service-icon"></span>Sheller Equipment Refurbishing</div><p>We restore and refurbish used peanut processing equipment. Contact us if you are interested in refurbished equipment.</p></div>
  <div class="service" style="left:26px;top:480px"><div class="service-pill"><span class="service-icon"></span>Equipment Manufacturing</div><p>We build custom vibratory conveyors and sizing shakers.</p></div>
  <div class="service" style="left:186px;top:480px"><div class="service-pill service-pill--dark"><span class="service-icon"></span>Customer Support</div><p>We provide excellent customer service and support for each of our clients.</p></div>
  <div class="service" style="left:340px;top:480px"><div class="service-pill"><span class="service-icon"></span>Welding &amp; Fabrication</div><p>We provide welding and fabrication for custom parts and equipment repair.</p></div>

  <div class="partner" style="left:18px;top:545px">WILMOT PENN</div>
  <div class="partner" style="left:117px;top:545px">HALVERN</div>
  <div class="partner" style="left:18px;top:578px;font-weight:500;font-size:11px">Brannock</div>
  <div class="partner" style="left:117px;top:578px">Keystone</div>
  <div class="abs" style="left:106px;top:548px;width:1px;height:56px;background:var(--line)"></div>
  <div class="abs" style="left:22px;top:576px;width:170px;height:1px;background:var(--line)"></div>

  <svg class="abs footer-shape" viewBox="0 0 490 93" aria-hidden="true">
    <polygon points="265,10 490,10 490,78 195,78" fill="#141414"/>
    <polygon points="257,4 490,4 490,10 265,10 195,78 187,78" fill="#1b4fa8"/>
    <polygon points="0,78 490,78 490,93 0,93" fill="#1b4fa8"/>
  </svg>
  <div class="abs contact" style="left:257px;top:572px;font-size:10.5px;line-height:12px">
    <svg width="10" height="10" viewBox="0 0 10 10"><circle cx="5" cy="5" r="5" fill="#37c2ec"/><circle cx="5" cy="4.2" r="1.6" fill="#141414"/></svg>418 W Mill Street
    &nbsp;<svg width="10" height="10" viewBox="0 0 10 10"><circle cx="5" cy="5" r="5" fill="#37c2ec"/><path d="M3.3 2.8l1 1-.5.7a3 3 0 0 0 1.7 1.7l.7-.5 1 1-.7.8A4.5 4.5 0 0 1 2.6 3.5z" fill="#141414"/></svg>(334) 555-0142<br>
    &nbsp;&nbsp;&nbsp;Ardenville, AL 36390
  </div>
  <div class="abs web" style="left:254px;top:600px;font-size:13px;letter-spacing:3.6px">www.<b>tovrik-inc</b>.com</div>
</section>

</body>
</html>
```